Dutch craft distillery needs labels designed for Gin bottle

We are a small craft distillery based in The Netherlands. We are currently producing only GIN. While we do have a logo for our distillery, we are still in search of a winning design for our Gin bottle. We are looking for something modern yet classy. Let your creativity run wild. Play around with colours, think out of the box….The winning designer will be challenged to create the coolest labels for the different flavours of Gin we will be producing in the near future. The label will maintain the same design elements throughout the design, but will also be able to differentiate each variety clearly. So for e.g. A flowery VosKamp Gin can have a pink label with a different description and a spicy VosKamp gin can have another colour with another description and so on. If the design really appeals to us, we might also invite the designer to do our website for us!

In a nutshell: It is a 500 ml bottle, (Please check the attachment so you get an idea as to what kind of bottle to imagine while making the labels). The bottle is going to have a light coloured wooden lid/cork to it. As of now we have a transparent seal to complete the sealing process once the bottling is done. The idea is that we will have two labels. One in the front and one behind. The size of the labels are as follows:

Front label: 102 x 76 mm the front label. (TO BE USED HORIZONTALLY). The details that we need on the front label are in a separate attachment.

Back label: The size for the label at the back of the bottle is: 76 x 51 mm (TO BE USED VERTICALLY) The information that needs to come on the label behind is also in the same document which is attached separately. The label behind will also have batch no. & date (Please refer to attachment to understand what I mean by batch no. date, distiller’s signature etc.) I have attached a picture of an already existing brand which has its batch number and distillers signature etc on it….so you can understand what I exactly mean by that. Please do not copy their design, this is purely to give you an idea as to what I mean by batch number and so on. The address of the distillery can be put horizontally, vertically, on the side along one border, or however you find appropriate. This is the address:
Berkenhoutlaan 41,
7311 KD, Hengelo.
The Netherlands.
www.voskamp.nl

Logo’s no drinking when pregnant, No driving and drinking, No drinking under the age of 18 need to be present on the label behind. Alternately, we can also have www.calm-sipping.com instead of the under 18 no alcohol sign, most alcohol bottles these days have it. Please let me know what else you would need from me for this. So be creative and do your best!

Thanks and regards, Marisol Venkataraghavan.

Target Market(s)

Largely males and females between 25-55 , the audience could even be slightly older.

Colors

Designer to choose colors to be used in the design.

Requirements
Must have
• 1) The labels need to be modern, yet classy, elite..
• 2) We need to specify the fact that we are a craft distillery and the gin is HANDMADE, using only the highest quality ingredients.
• 3) We at VosKamp live, breathe, dream, talk about our dream which is our distillery and its product. The label needs to bring home this point and should clearly specify and mention that it is produced and bottled in The Netherlands. Or handmade and bottled with love and passion in The Netherlands or something to that effect if it matches with the rest of the design.
• 4) The colours you chose must match in some way or the other with the colours used for the logo design.
Nice to have
• Would be nice to have colours and look bold, although not completely necessary.
Should not have
• What I definitely do not want is something too whacky like a skull or some kind of vague work of art. For the rest, I leave it upto you….!

```html
<!DOCTYPE html>
<html lang="en">
<head>
<meta charset="utf-8">
<title>VosKamp Premium London Dry Gin – Front Label</title>
<link rel="stylesheet" href="https://fonts.googleapis.com/css2?family=Arvo:wght@400;700&family=Kaushan+Script&family=Oswald:wght@500;600&family=Sancreek&display=swap">
<style>
  :root {
    --canvas-bg: #1b1b1c;
    --label-yellow: #f3d16a;
    --label-yellow-light: #fae7a4;
    --label-yellow-deep: #e9bf4e;
    --gin-red: #d6432c;
    --gin-red-dark: #b8341f;
    --ink: #262628;
    --ink-soft: #3b3b3e;
    --paper: #fff7e6;
    --ornament: #c9a548;
  }
  * { margin: 0; padding: 0; box-sizing: border-box; }
  html, body {
    width: 1200px;
    height: 2200px;
    overflow: hidden;
    background: var(--canvas-bg);
  }
  .front-label {
    position: absolute;
    left: 50px;
    top: 691px;
    width: 1100px;
    height: 817px;
    background: radial-gradient(ellipse at 50% 40%, var(--label-yellow-light) 0%, var(--label-yellow) 55%, var(--label-yellow-deep) 100%);
    overflow: hidden;
  }
  .label-art {
    position: absolute;
    inset: 0;
    width: 1100px;
    height: 817px;
  }
  .tagline {
    position: absolute;
    top: 86px;
    font-family: "Kaushan Script", cursive;
    font-size: 32px;
    line-height: 1;
    color: var(--ink);
  }
  .tagline--left { left: 170px; }
  .tagline--right { right: 170px; }
  .distillery-name {
    position: absolute;
    top: 78px;
    left: 0;
    width: 100%;
    text-align: center;
    font-family: "Oswald", sans-serif;
    font-weight: 600;
    color: var(--gin-red);
    line-height: 1;
  }
  .distillery-name .name-line { display: block; font-size: 64px; letter-spacing: 3px; }
  .distillery-name .type-line { display: block; font-size: 30px; letter-spacing: 6px; margin-top: 6px; color: var(--ink); }
  .claims {
    position: absolute;
    left: 360px;
    top: 640px;
    width: 550px;
    text-align: center;
    font-family: "Arvo", serif;
    color: var(--ink);
  }
  .claims .claim-natural {
    font-size: 35px;
    letter-spacing: 1px;
    line-height: 46px;
  }
  .claims .claim-pure {
    display: block;
    background: var(--ink);
    color: var(--paper);
    font-size: 31px;
    line-height: 42px;
    letter-spacing: 1px;
  }
  .spec-row {
    position: absolute;
    left: 360px;
    top: 742px;
    width: 550px;
    display: flex;
    justify-content: space-between;
    font-family: "Oswald", sans-serif;
    color: var(--ink);
    text-align: center;
  }
  .spec { flex: 1; line-height: 1; }
  .spec + .spec { border-left: 3px solid var(--ink); }
  .spec .spec-value { display: block; font-size: 32px; font-weight: 600; }
  .spec .spec-unit { display: block; font-size: 13px; font-weight: 500; letter-spacing: 1px; margin-top: 3px; }
  .spec--batch { flex: 1.6; }
</style>
</head>
<body>
  <main class="front-label">
    <svg class="label-art" viewBox="0 0 1100 817" xmlns="http://www.w3.org/2000/svg">
      <defs>
        <radialGradient id="rays-glow" cx="50%" cy="50%" r="50%">
          <stop offset="0%" stop-color="#fff6d4" stop-opacity="0.9"/>
          <stop offset="100%" stop-color="#fff6d4" stop-opacity="0"/>
        </radialGradient>
        <path id="badge-arc" d="M 146 700 A 76 76 0 0 1 298 700"/>
      </defs>

      <ellipse class="sunburst" cx="550" cy="120" rx="260" ry="140" fill="url(#rays-glow)" role="img" aria-label="Radiating sunburst behind the distillery name"/>

      <g class="frame" fill="none" stroke="var(--ink)">
        <rect x="22" y="22" width="1056" height="773" stroke-width="3"/>
        <rect x="32" y="32" width="1036" height="753" stroke-width="1.5"/>
      </g>

      <g class="corner-ornaments" fill="var(--ornament)" opacity="0.55">
        <rect x="42" y="42" width="100" height="76" rx="10" role="img" aria-label="Scrolled corner flourish"/>
        <rect x="958" y="42" width="100" height="76" rx="10" role="img" aria-label="Scrolled corner flourish"/>
        <rect x="42" y="699" width="100" height="76" rx="10" role="img" aria-label="Scrolled corner flourish"/>
        <rect x="958" y="699" width="100" height="76" rx="10" role="img" aria-label="Scrolled corner flourish"/>
      </g>

      <text class="product-name" x="550" y="440" text-anchor="middle" textLength="840" lengthAdjust="spacingAndGlyphs"
            font-family="Sancreek, serif" font-size="260" fill="var(--gin-red)">VOSKAMP</text>

      <g class="ribbon" transform="rotate(-7 640 530)">
        <polygon points="250,510 340,510 340,580 250,580 278,545" fill="var(--ink-soft)"/>
        <polygon points="940,480 1035,480 1007,515 1035,550 940,550" fill="var(--ink-soft)"/>
        <rect x="330" y="475" width="620" height="90" fill="var(--ink)"/>
        <text x="640" y="540" text-anchor="middle" textLength="540" lengthAdjust="spacingAndGlyphs"
              font-family="Oswald, sans-serif" font-weight="600" font-size="50" fill="var(--paper)">PREMIUM LONDON DRY GIN</text>
      </g>

      <g class="origin-badge">
        <circle cx="222" cy="700" r="94" fill="var(--gin-red)"/>
        <text font-family="Arvo, serif" font-size="17" fill="var(--paper)" text-anchor="middle">
          <textPath href="#badge-arc" startOffset="50%">Product of The Netherlands</textPath>
        </text>
        <rect x="196" y="690" width="52" height="64" rx="12" fill="var(--paper)" opacity="0.9" role="img" aria-label="Map outline of The Netherlands"/>
      </g>
    </svg>

    <p class="tagline tagline--left">Handcrafted</p>
    <p class="tagline tagline--right">Small batch</p>

    <h2 class="distillery-name">
      <span class="name-line">VOSKAMP</span>
      <span class="type-line">DISTILLERY</span>
    </h2>

    <div class="claims">
      <p class="claim-natural">100% NATURAL BOTANICALS</p>
      <p class="claim-pure">NO ARTIFICIAL FLAVOURING</p>
    </div>

    <div class="spec-row">
      <p class="spec"><span class="spec-value">43%</span><span class="spec-unit">ALC./VOL</span></p>
      <p class="spec spec--batch"><span class="spec-value">L100/2018</span><span class="spec-unit">BATCH NO.</span></p>
      <p class="spec"><span class="spec-value">750</span><span class="spec-unit">ML</span></p>
      <p class="spec"><span class="spec-value">50</span><span class="spec-unit">CL</span></p>
    </div>
  </main>
</body>
</html>
```